KV Group

We need a new website for our company and since we had a very good work done for our logo in this site, we're back for the entire job.

Our company name is Marlowe Capital Group. We're adding files of examples of what we have done today. In my opinion we need a more attention lock in the site but yet financial simple work.

Our files (attached) will let you know what we have so far. We need a complete change but the colours should be the same, however you can change them not running away to far from the original, and of course matching with the logo.

We need examples for 3 kind of layouts.

- A HOME welcome layout
- An internal Layout with sidebar
- And internal Layout wide

We can buy image licenses if needed for assets.
Actually there are 5 slide images placed on the Welcome HOME, we need those there, but you can improve with better images to match the new website!!!

Target Market(s)

Clients looking for financial advisers, tax and funds specialist, currency advisers

Industry/Entity Type

Financial

Requirements
Must have
• all the fonts must be in accordance with the financial market sites........the welcome home page must be precise, neat and information accurate........the menu should be elegant........main focus on the Home page, should be also the PRIVATE ACCESS box log in.......

```html
<!DOCTYPE html>
<html lang="en">
<head>
<meta charset="utf-8">
<title>Marlowe Capital Group — Home</title>
<link rel="stylesheet" href="https://fonts.googleapis.com/css2?family=Source+Sans+3:wght@700&family=Noto+Serif&display=swap">
<style>
  :root {
    --brand-orange: #f47b20;
    --ink: #111111;
    --frame: #050505;
    --panel: rgba(255, 255, 255, 0.42);
    --hero-light: #e4e7ea;
    --hero-mid: #c7d3d9;
    --hero-dark: #6f7a80;
    --rail: #8a8f93;
    --rail-active: #ffffff;
  }
  * { margin: 0; padding: 0; box-sizing: border-box; }
  html, body { width: 1200px; height: 598px; overflow: hidden; }
  body { position: relative; font-family: "Noto Serif", Georgia, serif; color: var(--ink); }

  .hero-photo {
    position: absolute; inset: 0;
    background:
      radial-gradient(ellipse 55% 60% at 70% 30%, rgba(255,255,255,0.55), transparent 70%),
      linear-gradient(200deg, var(--hero-mid) 0%, var(--hero-light) 45%, #d2d4d4 70%, var(--hero-dark) 100%);
  }

  .brand {
    position: absolute; left: 206px; top: 88px;
    display: flex; align-items: center; gap: 10px;
  }
  .brand-mark { width: 22px; height: 22px; background: var(--brand-orange); }
  .brand-name {
    font-family: "Source Sans 3", "Source Sans Pro", Arial, sans-serif;
    font-weight: 700; font-size: 24px; letter-spacing: 0.5px; color: #2a2a2a;
  }

  .private-access {
    position: absolute; left: 956px; top: 42px; width: 44px; height: 44px;
    border: 1.5px solid var(--frame);
    display: flex; align-items: center; justify-content: center;
  }

  .hero-card {
    position: absolute; left: 202px; top: 197px; width: 797px; height: 270px;
    border: 4px solid var(--frame); background: var(--panel);
    text-align: center;
  }
  .hero-title {
    margin-top: 48px;
    font-family: "Source Sans 3", "Source Sans Pro", Arial, sans-serif;
    font-weight: 700; font-size: 56px; line-height: 59px;
    color: var(--brand-orange); text-transform: uppercase;
  }
  .hero-text {
    margin: 22px auto 0; width: 640px;
    font-size: 15.5px; line-height: 22px;
  }

  .slide-rail {
    position: absolute; left: 484px; top: 550px;
    display: flex; gap: 5px; align-items: center;
  }
  .slide-rail span { display: block; width: 73px; height: 1.5px; background: var(--rail); }
  .slide-rail span.is-active { height: 3px; background: var(--rail-active); }
</style>
</head>
<body>
  <div class="hero-photo" role="img" aria-label="Blurred photo of business people talking in a bright office, laptop on the desk in front"></div>

  <div class="brand">
    <span class="brand-mark"></span>
    <span class="brand-name">Marlowe Capital Group</span>
  </div>

  <div class="private-access" aria-label="Private access login">
    <svg width="18" height="10" viewBox="0 0 18 10">
      <circle cx="4" cy="5" r="3.5" fill="var(--brand-orange)"/>
      <rect x="6" y="4" width="11" height="2" fill="var(--brand-orange)"/>
      <rect x="13" y="6" width="2" height="2.5" fill="var(--brand-orange)"/>
    </svg>
  </div>

  <section class="hero-card">
    <h1 class="hero-title">Teamwork for your<br>benefit</h1>
    <p class="hero-text">Our dedicated Private Bankers, will proactively keep you up to date with the most relevant information.</p>
  </section>

  <nav class="slide-rail" aria-label="Slides">
    <span></span>
    <span class="is-active"></span>
    <span></span>
  </nav>
</body>
</html>
```